New Packaging Design Project

Wine packaging redesign. Retail partner requested a redesign of a private label wine. The old label is attached. Our partner liked the Lantern and Briar label and wanted something similar. There will be a logo added to the top of the label

Went on vacation/holiday

```html
<!DOCTYPE html>
<html lang="en">
<head>
<meta charset="UTF-8">
<title>Ashford Hollow Red Blend Label</title>
<link href="https://fonts.googleapis.com/css2?family=Hind:wght@300;400;600&display=swap" rel="stylesheet">
<style>
  :root {
    --backdrop: #c6c6c6;
    --label-paper: #e6e6e6;
    --ink: #2b2b2b;
    --ink-soft: #4a4a4a;
    --art-light: #d9d9d9;
    --art-dark: #a9a9a9;
  }
  * { margin: 0; padding: 0; box-sizing: border-box; }
  html, body {
    width: 1200px;
    height: 824px;
    overflow: hidden;
    background: var(--backdrop);
  }
  .canvas {
    width: 1200px;
    height: 824px;
    display: flex;
    align-items: center;
    justify-content: center;
  }
  .wine-label {
    width: 600px;
    height: 560px;
    background: var(--label-paper);
    display: flex;
    flex-direction: column;
    align-items: center;
    padding-top: 64px;
    font-family: "Hind", sans-serif;
    color: var(--ink);
  }
  .brand-name {
    font-weight: 600;
    font-size: 46px;
    letter-spacing: 0.14em;
    text-transform: uppercase;
    line-height: 1;
  }
  .landscape-art {
    width: 300px;
    height: 190px;
    margin-top: 40px;
    background: linear-gradient(180deg, var(--art-light) 0%, var(--art-dark) 100%);
  }
  .wine-style {
    margin-top: 34px;
    font-weight: 400;
    font-size: 22px;
    letter-spacing: 0.04em;
    text-transform: uppercase;
  }
  .grape-list {
    margin-top: 14px;
    text-align: center;
    font-weight: 300;
    font-size: 15px;
    letter-spacing: 0.04em;
    line-height: 1.5;
    text-transform: uppercase;
    color: var(--ink-soft);
  }
  .grape-list .divider { padding: 0 8px; }
  .vintage {
    margin-top: 16px;
    font-weight: 300;
    font-size: 14px;
    letter-spacing: 0.08em;
    color: var(--ink-soft);
  }
</style>
</head>
<body>
  <main class="canvas">
    <section class="wine-label">
      <h1 class="brand-name">Ashford Hollow</h1>
      <div class="landscape-art" role="img" aria-label="Line drawing of a coastal valley with hills, trees, sailboats on the water and birds in the sky"></div>
      <h2 class="wine-style">Red Blend</h2>
      <p class="grape-list">
        Merlot<span class="divider">|</span>Cabernet Sauvignon<br>
        Cabernet Franc<span class="divider">|</span>Petit Verdot<span class="divider">|</span>Malbec
      </p>
      <p class="vintage">2018</p>
    </section>
  </main>
</body>
</html>
```